Business Card Design Project

Require a business card for a swing band called "Velvet Brass Parade". We are a 6 piece band that performs at events and corporate functions. Our music is great for dancing to or just providing a classy background atmosphere for people to enjoy. Final design should communicate professionalism and style with a hint of fun.

Sorry, just realised that it needs to be single sided only. Also, no rounded edges.

Industry/Entity Type

Events

Requirements
Must have
• Contact number: 0438 216 903
email address: velvetbrassparade@mailbox-demo.net
Website details: www.velvetbrassparade-demo.com

```html
<!DOCTYPE html>
<html lang="en">
<head>
<meta charset="utf-8">
<title>Velvet Brass Parade — Business Card</title>
<link rel="stylesheet" href="https://fonts.googleapis.com/css2?family=Parisienne&family=Carlito&display=swap">
<style>
  :root {
    --card-brown: #6b3e16;
    --gold: #f8c400;
    --copper: #c47a2c;
    --ornament: #4a2a0e;
  }
  html, body {
    margin: 0;
    padding: 0;
    overflow: hidden;
    background: var(--card-brown);
  }
  .card {
    position: relative;
    width: 754px;
    height: 1200px;
    background: var(--card-brown);
    overflow: hidden;
  }
  .corner-ornament {
    position: absolute;
    width: 100px;
    height: 100px;
    background: var(--ornament);
    opacity: 0.55;
  }
  .corner-ornament.top-left { left: 19px; top: 19px; }
  .corner-ornament.top-right { right: 19px; top: 19px; }
  .corner-ornament.bottom-left { left: 19px; bottom: 19px; }
  .corner-ornament.bottom-right { right: 19px; bottom: 19px; }

  .band-name {
    position: absolute;
    left: 110px;
    top: 250px;
    width: 540px;
    margin: 0;
    font-family: "Parisienne", cursive;
    font-weight: 400;
    font-size: 124px;
    line-height: 1.25;
    color: var(--gold);
  }
  .band-name .line { display: block; }
  .band-name .line.second { text-align: right; }

  .music-notes {
    position: absolute;
    left: 30px;
    top: 697px;
    width: 245px;
    height: 360px;
    background: linear-gradient(160deg, var(--copper), #a8621f);
    opacity: 0.7;
  }

  .contact {
    position: absolute;
    left: 312px;
    top: 945px;
    margin: 0;
    padding: 0;
    list-style: none;
    font-family: "Carlito", "Calibri", sans-serif;
    font-size: 25px;
    line-height: 38px;
    color: var(--gold);
  }
</style>
</head>
<body>
  <main class="card">
    <div class="corner-ornament top-left" role="img" aria-label="Decorative corner flourish"></div>
    <div class="corner-ornament top-right" role="img" aria-label="Decorative corner flourish"></div>
    <div class="corner-ornament bottom-left" role="img" aria-label="Decorative corner flourish"></div>
    <div class="corner-ornament bottom-right" role="img" aria-label="Decorative corner flourish"></div>

    <h1 class="band-name">
      <span class="line">Velvet Brass</span>
      <span class="line second">Parade</span>
    </h1>

    <div class="music-notes" role="img" aria-label="Illustration of dancing musical notes with bass and treble clefs"></div>

    <ul class="contact">
      <li class="contact-phone">0438 216 903</li>
      <li class="contact-email">velvetbrassparade@mailbox-demo.net</li>
      <li class="contact-web">www.velvetbrassparade-demo.com</li>
    </ul>
  </main>
</body>
</html>
```